Sunmeadow Home Care Business Card

We are a home care company customizing in personal care services. Our personal care service is different because our mission is to provide the most effective care while enhancing quality of life. We strive to make everyday our client's best day. I would like a very classic and/or retro feel. I don't like clip art.

Target Market(s)

doctor's offices; potential clients

Industry/Entity Type

Business

Contact Information for Business Card

jdalton@sunmeadowhc.example(919) 480-15904000 Blue Ridge Road, Suite 101Raleigh, NC 27612www.SunmeadowHC.example

Requirements
Must have
• classic and/or retro feel. Very caring.
Should not have
• Clip art

```html
<!DOCTYPE html>
<html lang="en">
<head>
<meta charset="utf-8">
<title>Sunmeadow Home Care Business Card</title>
<link rel="stylesheet" href="https://fonts.googleapis.com/css2?family=Source+Sans+3:wght@400;600&display=swap">
<style>
  :root {
    --backdrop: #0b2a2d;
    --card: #1a1714;
    --card-edge: #0f0d0b;
    --frame: #6f7a64;
    --dots: #cfcbbf;
    --gold: #a98552;
    --gold-light: #c9a56c;
    --name-green: #93c25a;
  }
  html, body {
    margin: 0;
    padding: 0;
    width: 1200px;
    height: 689px;
    overflow: hidden;
    background: var(--backdrop);
  }
  .canvas {
    position: relative;
    width: 1200px;
    height: 689px;
    background: radial-gradient(ellipse at center, #10353a 0%, var(--backdrop) 75%);
    font-family: "Source Sans 3", "Myriad Pro", sans-serif;
  }
  .card {
    position: absolute;
    left: 46px;
    top: 46px;
    width: 1112px;
    height: 597px;
    box-sizing: border-box;
    border: 2px solid var(--frame);
    outline: 1px solid #3e4a40;
    outline-offset: 3px;
    background: radial-gradient(ellipse at 50% 45%, #221d18 0%, var(--card) 55%, var(--card-edge) 100%);
  }
  .dotted-frame {
    position: absolute;
    left: 29px;
    top: 29px;
    right: 27px;
    bottom: 27px;
    border: 2px dotted var(--dots);
    opacity: 0.85;
  }
  .company-name {
    position: absolute;
    left: 0;
    right: 0;
    top: 176px;
    margin: 0;
    text-align: center;
    font-weight: 600;
    font-size: 64px;
    line-height: 1;
    letter-spacing: 0.5px;
    color: var(--name-green);
  }
  .contact-list {
    position: absolute;
    left: 0;
    right: 0;
    top: 357px;
    margin: 0;
    padding: 0;
    list-style: none;
  }
  .contact-row {
    position: relative;
    height: 47px;
    display: flex;
    align-items: center;
    justify-content: center;
  }
  .contact-text {
    font-size: 23px;
    line-height: 1;
    color: var(--gold);
    white-space: nowrap;
  }
  .rule {
    position: absolute;
    top: 50%;
    width: 114px;
    height: 8px;
    margin-top: -4px;
  }
  .rule-left { left: 165px; }
  .rule-right { left: 843px; }
</style>
</head>
<body>
<div class="canvas">
  <div class="card">
    <div class="dotted-frame"></div>

    <h1 class="company-name">Sunmeadow Home Care, Inc.</h1>

    <ul class="contact-list">
      <li class="contact-row">
        <svg class="rule rule-left" viewBox="0 0 114 8" aria-hidden="true"><line x1="0" y1="2" x2="114" y2="2" stroke="var(--gold-light)" stroke-width="1.4"/><line x1="10" y1="6" x2="114" y2="6" stroke="var(--gold)" stroke-width="1.4"/></svg>
        <span class="contact-text">2700 Copper Finch Lane, Suite 101 Raleigh, NC 27612</span>
        <svg class="rule rule-right" viewBox="0 0 114 8" aria-hidden="true"><line x1="0" y1="2" x2="114" y2="2" stroke="var(--gold-light)" stroke-width="1.4"/><line x1="0" y1="6" x2="104" y2="6" stroke="var(--gold)" stroke-width="1.4"/></svg>
      </li>
      <li class="contact-row">
        <svg class="rule rule-left" viewBox="0 0 114 8" aria-hidden="true"><line x1="0" y1="2" x2="114" y2="2" stroke="var(--gold-light)" stroke-width="1.4"/><line x1="10" y1="6" x2="114" y2="6" stroke="var(--gold)" stroke-width="1.4"/></svg>
        <span class="contact-text">(555) 302-7741</span>
        <svg class="rule rule-right" viewBox="0 0 114 8" aria-hidden="true"><line x1="0" y1="2" x2="114" y2="2" stroke="var(--gold-light)" stroke-width="1.4"/><line x1="0" y1="6" x2="104" y2="6" stroke="var(--gold)" stroke-width="1.4"/></svg>
      </li>
      <li class="contact-row">
        <svg class="rule rule-left" viewBox="0 0 114 8" aria-hidden="true"><line x1="0" y1="2" x2="114" y2="2" stroke="var(--gold-light)" stroke-width="1.4"/><line x1="10" y1="6" x2="114" y2="6" stroke="var(--gold)" stroke-width="1.4"/></svg>
        <span class="contact-text">jdalton@sunmeadowhc.example</span>
        <svg class="rule rule-right" viewBox="0 0 114 8" aria-hidden="true"><line x1="0" y1="2" x2="114" y2="2" stroke="var(--gold-light)" stroke-width="1.4"/><line x1="0" y1="6" x2="104" y2="6" stroke="var(--gold)" stroke-width="1.4"/></svg>
      </li>
      <li class="contact-row">
        <svg class="rule rule-left" viewBox="0 0 114 8" aria-hidden="true"><line x1="0" y1="2" x2="114" y2="2" stroke="var(--gold-light)" stroke-width="1.4"/><line x1="10" y1="6" x2="114" y2="6" stroke="var(--gold)" stroke-width="1.4"/></svg>
        <span class="contact-text">www.SunmeadowHC.example</span>
        <svg class="rule rule-right" viewBox="0 0 114 8" aria-hidden="true"><line x1="0" y1="2" x2="114" y2="2" stroke="var(--gold-light)" stroke-width="1.4"/><line x1="0" y1="6" x2="104" y2="6" stroke="var(--gold)" stroke-width="1.4"/></svg>
      </li>
    </ul>
  </div>
</div>
</body>
</html>
```